Tri Fold Brochure, Large Postcard, Letter head & Envelope For Real Estate Broker.
Cohesive Marketing Materials for Real Estate Broker in Rhode Island.
Thank You Creative!
Hi,
I have add Harlow Pennington logo in footer in my both design options please have a look.
Thanks.
Rewrote this section:
{HEADLINE} Native Son...
Being a committed community member, husband and devoted father are three key focal points in his world. In fact, his daughter Molly is a never-ending source of inspiration and happiness. Whether spending a day on Gull Island with wife Lorraine and Moll, or taking Molly to play golf, Tom cherishes those special moments spent with family.
Text for Brochure:
{HEADLINE} The Fine Art of Representing You...
Tom has been privileged to represent the owners of a diverse range of homes from waterfront showpieces to cozy Cape Cod's and everything in between.
Tom regards you and your property with the highest priority and respect and he guarantee's everything he does with the "Golden Rule" promise.
"I will be your trusted advisor navigating your home purchase and/or home sale for you as your advocate. If for any reason you are unsatisfied with my representation you are free to fire me, no catch's & no small print".
Our clients love what we do and we are confident you will as well. Our goal is to become YOUR Realtor and the only Realtor you want to refer to your family and friends. Put us to the Test!
{HEADLINE} There's a Saying: Conceive It, Believe It, Achieve It!
Just spend a day with Tom Ashby and you will see a perfect example of the power of attitude. This upbeat, native Rhode Islander approaches everything in life with an enthusiasm that is quite infectious. But where does Tom Ashby draw so much energy from—what makes him tick?
Being a committed community member and devoted father to his daughter Molly are two key focal points in his world. In fact, his daughter Molly is a never-ending source of inspiration and happiness. Whether spending a day on Gull Island, or taking Molly to play golf, Tom cherishes those special moments spent with her.
{HEADLINE} Children Bring a New Perspective on Life...
“Having a child rejuvenates you,” Tom says. “Things take on a fresh new perspective. It’s a joy to see the world through Molly’s eyes. Even the simplest things I used to take for granted now become exciting again because I can experience them with Moll.”
{HEADLINE} The Dreams and Aspirations of a Great Place, A Great People...
A native of Rhode Island, After graduating from East Marlow High School at the age of 17, Tom left his idyllic hometown of Pelton to serve with the Coastal Defense Volunteer Corps. Tom has proved that the old adage "You Cant Go Home Again" doesn't apply. After years away with the Marines and then building a large Real Estate practice in Southern Virginia, Tom and his family have come home to Rhode Island where it all started.
Tom wouldn’t dream of raising his daughter anywhere else. Surrounded by family, He believes there’s a quality of life here that begins with the ideals of its great people. “Rhode Island never changes in my view, we are a community of diverse backgrounds and cultures forged by the ocean and the coast and our rich history". "Our values, dreams and aspirations just seem to be the same , true and solid goals that our parents and grandparents strived for,” Tom explains. For Rhode Island residents one of the top goals seems to be the American Dream of home ownership. And that’s an area where Tom has become quite an authority—his other passion is his career as a real estate professional. In fact, this very passion has driven him to the top of his field. His nationally renowned performance is the direct result of his extensive knowledge and expertise backed by an unwavering commitment to go the distance for each client.
{HEADLINE} From Chubby Kid to Wrestling Champ...
But Tom will be the first to tell you that passion alone won’t guarantee success. Tom is a true believer in—and a perfect example of—the Yankee hard work ethic. Growing up as a overweight kid things weren’t handed to Tom, he had to struggle for most accomplishments. As a teen, Tom had a small dream to be the top wrestler in the area. He knew desire alone wasn't enough so he sought out the best wrestlers in the country to learn what they did to be so successful. Tom worked everyday to become just like the wrestlers he aspired to. His hard work and intense training paid off and Tmo went on to be a All State wrestler at East Marlow High School and a All New England and All American wrestler representing the state of Rhode Island at the Youth Union Grapple Series in Iowa.
Tom went on to represent the Coastal Defense Volunteer Corps in Greco Roman wrestling cumulating his wrestling career by winning the Service Branch Grapple Finals beating the formally unbeaten All Fleet heavyweight in the finals. Tom attributes his success on the mat to hard work, persistence and the techniques he learned from those who had gone before him.
{HEADLINE} Meet Tom, The Agent People love to Refer!
The road to becoming a top homeseller was not an easy one for Tom, either. From day one, Tom immersed himself with his typical zeal, taking every real estate class he could find, reading every book on the subject he could get his hands on, and spending hours studying with some of the top agents in the country.
{HEADLINE} Mastering His Craft: Day-To-Day Victories...
But true to form, Tom’s hard work eventually paid off. He started doing innovative personal marketing and set up systems to ensure outstanding service. Soon Tom was breaking records with his phenomenal performance. Tom is flattered by the requests he receives from companies and agents to share some of the secrets to his success. But to Tom, the status and accolades he’s earned in his profession aren’t as rewarding as the satisfying feeling he gets when he helps families achieve their dreams. “I work hard to master my craft,” Tom states, “Because so much is at stake when my clients have to sell an important part of their world. I want each of my clients to be confident of two things: they are working with the best and that I will do everything within my power to help them become successful.”
{HEADLINE} Reach Your Dreams With Tom Ashby By Your Side...
It makes perfect sense: you need to buy or sell your home, you want to be as successful as you can possibly be. That’s why you should work with Tom Ashby. Spend a few moments talking with Tom and see for yourself just how much he loves his work, and more importantly, how much of a difference this enthusiasm can make in your pursuit of the American Dream in the Ocean State...
{HEADLINE} In Conclusion...
Never losing sight of what is most important to our clients success, the fact that the majority of business is based on referrals from satisfied clients is a telling sign that Toms style of service is anything but standard. He often builds long tern relationships with his clients and becomes a trusted advisor and a friend. Whether buying or selling, Tom has the market knowledge, business savvy, care and dedication to help you make the most of your real estate opportunities.
I am working on the text for the brochure but most likely it will come after I pick the winning the design to be inserted after award.

```html
<!DOCTYPE html>
<html lang="en">
<head>
<meta charset="utf-8">
<title>Tom Ashby – Marketing Suite</title>
<link href="https://fonts.googleapis.com/css2?family=Cormorant+Garamond:wght@500;600;700&family=Lato:wght@400;700&display=swap" rel="stylesheet">
<style>
  :root{
    --gold:#c69c62;
    --gold-dark:#a97f45;
    --red:#b3262c;
    --cream:#f6eee2;
    --paper:#ffffff;
    --ink:#4a3a28;
    --caption:#8a8a8a;
    --photo-sea:linear-gradient(180deg,#9fb8c6 0%,#b9c9b0 55%,#6f8a4c 100%);
    --photo-house:linear-gradient(180deg,#a9bfcf 0%,#c9cdc8 45%,#7b8f5a 100%);
    --photo-room:linear-gradient(135deg,#8a2f1f 0%,#c0663a 50%,#5b2416 100%);
    --photo-lawn:linear-gradient(180deg,#cfd8da 0%,#92a86a 60%,#5e7a3a 100%);
    --photo-portrait:linear-gradient(180deg,#6e7f8e 0%,#3f4a55 100%);
  }
  *{box-sizing:border-box;margin:0;padding:0}
  html,body{width:1200px;height:473px;overflow:hidden;background:#fff}
  body{position:relative;font-family:"Lato",sans-serif;color:var(--ink)}
  .piece{position:absolute;overflow:hidden}
  .caption{position:absolute;font:400 5px "Lato",sans-serif;color:var(--caption);letter-spacing:.3px}
  .photo{position:absolute}
  .sea{background:var(--photo-sea)} .house{background:var(--photo-house)}
  .room{background:var(--photo-room)} .lawn{background:var(--photo-lawn)}
  .portrait{background:var(--photo-portrait)}
  .brand{position:absolute;display:flex;align-items:center;gap:4px;font-family:"Cormorant Garamond",serif;font-weight:600;color:var(--cream)}
  .brand .mark{width:9px;height:9px;border:1px solid currentColor}
  .heading{position:absolute;font-family:"Cormorant Garamond",serif;font-weight:700;color:var(--cream);line-height:1.1}
  .body-copy{position:absolute;font-size:5px;line-height:1.45;color:var(--cream)}
  .faint-mark{position:absolute;border:2px solid #efe6d8;background:#faf6f0}

  /* tri-fold brochure */
  .brochure{left:7px;width:300px;height:226px;display:flex;background:var(--gold)}
  .brochure.outside{top:9px}
  .brochure.inside{top:242px}
  .panel{position:relative;width:100px;height:100%;border-right:1px solid var(--gold-dark)}
  .panel:last-child{border-right:0}

  /* letterhead */
  .letterhead{left:319px;top:19px;width:233px;height:281px;background:var(--paper);border:1px solid #ddd}
  .letterhead .logo-block{position:absolute;left:14px;top:0;width:40px;height:42px;background:var(--gold)}
  .letterhead .rule{position:absolute;left:0;right:0;bottom:20px;height:2px;background:var(--red)}
  .letterhead .footer{position:absolute;left:0;right:0;bottom:0;height:18px;background:var(--gold);font-size:5px;color:var(--cream);display:flex;align-items:center;justify-content:center}

  /* envelopes */
  .envelope{background:var(--paper);border:1px solid #ddd}
  .envelope.business{left:319px;top:313px;width:238px;height:106px}
  .envelope.business .logo-block{position:absolute;left:8px;top:0;width:44px;height:48px;background:var(--gold)}
  .envelope.note{left:883px;top:9px;width:305px;height:154px}
  .envelope.note .rule{position:absolute;left:0;right:0;top:0;height:3px;background:var(--red)}
  .return-address{position:absolute;font-size:5px;line-height:1.5;color:var(--ink)}

  /* postcards */
  .postcard{left:580px;width:286px;background:var(--gold)}
  .postcard.front{top:9px;height:154px}
  .postcard.back{top:175px;height:161px}
  .band{position:absolute;left:0;right:0;background:var(--red);color:var(--cream);font-family:"Cormorant Garamond",serif;font-weight:600;display:flex;align-items:center}
  .stamp{position:absolute;right:10px;top:10px;width:26px;height:30px;border:1px solid var(--cream)}
  .address-line{position:absolute;right:12px;width:110px;height:1px;background:var(--cream)}
</style>
</head>
<body>

<!-- Tri-fold brochure, outside -->
<span class="caption" style="left:7px;top:2px">Outside Panels</span>
<section class="piece brochure outside">
  <div class="panel">
    <div class="photo portrait" role="img" aria-label="Portrait of the broker" style="left:8px;top:8px;width:24px;height:30px"></div>
    <h2 class="heading" style="left:36px;top:14px;font-size:9px">Meet Tom</h2>
    <p class="body-copy" style="left:8px;top:46px;width:84px">Tom Ashby is a native Rhode Islander who brings energy and care to every client.</p>
    <div class="photo sea" role="img" aria-label="Coastal landscape with water and grass" style="left:6px;top:150px;width:88px;height:64px"></div>
  </div>
  <div class="panel">
    <h2 class="heading" style="left:8px;top:10px;font-size:9px">Native Son</h2>
    <p class="body-copy" style="left:8px;top:26px;width:84px">A committed community member and devoted father, Tom cherishes days on Gull Island with family.</p>
    <div class="photo lawn" role="img" aria-label="Seaside lawn with Adirondack chairs" style="left:6px;top:130px;width:88px;height:84px"></div>
  </div>
  <div class="panel">
    <div class="photo house" role="img" aria-label="Shingle-style waterfront home on a grassy bluff" style="left:0;top:0;width:100px;height:90px"></div>
    <div class="brand" style="left:26px;top:100px;font-size:10px"><span class="mark"></span>Tom Ashby</div>
    <p class="body-copy" style="left:0;top:118px;width:100px;text-align:center">Harlow Pennington<br>401.555.0142<br>tom@tidewaterhomes.com</p>
    <p class="heading" style="left:0;top:160px;width:100px;text-align:center;font-size:8px;color:var(--red)">Honesty &amp; Integrity</p>
  </div>
</section>

<!-- Tri-fold brochure, inside -->
<span class="caption" style="left:7px;top:235px">Inside Panels</span>
<section class="piece brochure inside">
  <div class="panel">
    <h2 class="heading" style="left:8px;top:8px;width:84px;font-size:8px">The Fine Art of Representing You</h2>
    <div class="photo lawn" role="img" aria-label="White chairs on a lawn overlooking the sea" style="left:6px;top:34px;width:88px;height:58px"></div>
    <p class="body-copy" style="left:8px;top:98px;width:84px">Tom has represented homes from waterfront showpieces to cozy Capes and everything between.</p>
    <div class="photo sea" role="img" aria-label="Rolling coastal fields" style="left:6px;top:160px;width:88px;height:56px"></div>
  </div>
  <div class="panel">
    <div class="photo room" role="img" aria-label="Warm wood-panelled dining room interior" style="left:0;top:0;width:100px;height:100px"></div>
    <h2 class="heading" style="left:8px;top:108px;width:84px;font-size:8px">Conceive It, Believe It, Achieve It!</h2>
    <p class="body-copy" style="left:8px;top:132px;width:84px">Spend a day with Tom and you will see the power of attitude in action.</p>
  </div>
  <div class="panel">
    <h2 class="heading" style="left:8px;top:10px;font-size:8px">In Conclusion</h2>
    <p class="body-copy" style="left:8px;top:24px;width:84px">Most business comes from referrals by satisfied clients, a sign of Tom's service.</p>
    <div class="photo house" role="img" aria-label="Coastal home and garden" style="left:6px;top:110px;width:88px;height:50px"></div>
    <div class="photo sea" role="img" aria-label="Shoreline view" style="left:6px;top:166px;width:88px;height:50px"></div>
  </div>
</section>

<!-- Letterhead -->
<span class="caption" style="left:319px;top:12px">Letterhead</span>
<section class="piece letterhead">
  <div class="logo-block"><div class="brand" style="left:5px;top:16px;font-size:6px"><span class="mark" style="width:6px;height:6px"></span>Tom Ashby</div></div>
  <div class="faint-mark" style="left:76px;top:80px;width:80px;height:80px"></div>
  <div class="rule"></div>
  <div class="footer">12 Harbor Lane · Pelton, RI 02852 · 401.555.0142</div>
</section>

<!-- #10 envelope -->
<span class="caption" style="left:319px;top:306px">#10 Envelope</span>
<section class="piece envelope business">
  <div class="logo-block"><div class="brand" style="left:6px;top:19px;font-size:6px"><span class="mark" style="width:6px;height:6px"></span>Tom Ashby</div></div>
  <p class="return-address" style="left:8px;top:52px">12 Harbor Lane<br>Pelton, RI 02852</p>
  <div class="faint-mark" style="left:170px;top:30px;width:46px;height:46px"></div>
</section>

<!-- Postcard front -->
<span class="caption" style="left:580px;top:2px">Postcard Front</span>
<section class="piece postcard front">
  <div class="band" style="top:0;height:22px;padding-left:92px;font-size:10px">Honesty | Expertise | Teamwork</div>
  <div class="photo room" role="img" aria-label="Broker standing in an elegant home interior" style="left:82px;top:22px;width:204px;height:110px"></div>
  <div class="brand" style="left:10px;top:70px;font-size:10px"><span class="mark"></span>Tom Ashby</div>
  <div class="band" style="left:8px;right:auto;top:88px;width:66px;height:14px;padding-left:5px;font-size:7px">Selling Homes</div>
  <div class="band" style="top:132px;height:22px;justify-content:flex-end;padding-right:12px;font-size:9px">Your Trusted Advisor</div>
</section>

<!-- Postcard back -->
<span class="caption" style="left:580px;top:168px">Postcard Back</span>
<section class="piece postcard back">
  <div class="photo sea" role="img" aria-label="Coastal scenery" style="left:8px;top:8px;width:44px;height:34px"></div>
  <div class="photo house" role="img" aria-label="Seaside home" style="left:56px;top:8px;width:44px;height:34px"></div>
  <div class="photo lawn" role="img" aria-label="Garden lawn" style="left:8px;top:46px;width:44px;height:34px"></div>
  <p class="body-copy" style="left:10px;top:92px;width:110px;font-size:6px">Thinking of selling? Call Tom today.<br>tidewaterhomes.com</p>
  <div class="stamp"></div>
  <div class="address-line" style="top:80px"></div>
  <div class="address-line" style="top:96px"></div>
  <div class="address-line" style="top:112px"></div>
  <div class="address-line" style="top:128px"></div>
</section>

<!-- Note envelope -->
<span class="caption" style="left:883px;top:2px">A7 Envelope</span>
<section class="piece envelope note">
  <div class="rule"></div>
  <p class="return-address" style="left:166px;top:78px">Tom Ashby<br>12 Harbor Lane<br>Pelton, RI 02852</p>
  <div class="faint-mark" style="left:232px;top:66px;width:50px;height:56px"></div>
</section>

</body>
</html>
```